"Velvet Crest" sexual performance enhancement pill bottle label needed.

This should be interesting...

I am starting a line of sexual performance enhancement products. This will be the first of several products basically. Keep in mind, I am the type of business person to stay with one company for years if they provide me with quality work.

This particular product is a male sexual performance pill. The name of the product is "Velvet Crest." The packaging of the pills are a black bottle with a white top. Label on the product example would be perfect but at a minimum I have attached a "template" for your guidance.

Some of the technical aspects of this are as follows:

-File Format: Illustrator CS6 is preferred. (Winner must provide artwork in layer and can not flatten artwork.)
-Resolution: 300 dpi minimum
-Bleed: 1/16th (0.0625") inch from edge of label
-Color Mode: CMYK only or must be converted to CMYK for final production

Lastly, this is your project as a designer, artist, creator, this is essentially a piece of you that will be sold and known by thousands of people. I have no color scheme that I prefer, just use the template and follow the layout. If you have any further questions, please feel free to contact me at any time.
Updates

Quick note on the product and what it does: -Powerful, long lasting, harder erections -Works in a minutes and last for hours -Enhances sexual desire and drive Thank you for your ideas...

Project Deadline Extended
Reason: We decided to extent the project for a few more days to let the last few concepts come in. So far things are looking really good and we definitely have seen some amazing designs. Thank you for your hard work and amazing creativity. Looking forward to seeing what we have come in the next couple of day. Very respectfully, Brock

ONLY THREE DAYS LEFT!!!! Please submit your ideas as soon as possible. And as always, thank you for your help!!! V/r, Brock

Industry/Entity Type

Graphic Design

```html
<!DOCTYPE html>
<html lang="en">
<head>
<meta charset="utf-8">
<title>Velvet Crest – Bottle Label</title>
<link href="https://fonts.googleapis.com/css2?family=Exo+2:ital,wght@0,600;0,700;1,800&display=swap" rel="stylesheet">
<style>
  :root {
    --stage: #e9e9e9;
    --label-black: #060608;
    --silver-light: #f2f2f2;
    --silver-mid: #bdbdbd;
    --silver-dark: #8a8a8a;
    --band-text: #1f3b40;
    --name-silver: #e3e2ea;
    --neon-cyan: #22c6e6;
    --neon-magenta: #e0259c;
    --skin-warm: #c98d73;
    --skin-shadow: #5a2a35;
    --white: #ffffff;
    --ribbon-text: #161616;
  }
  * { box-sizing: border-box; margin: 0; padding: 0; }
  html, body {
    width: 1200px;
    height: 960px;
    overflow: hidden;
    background: var(--stage);
    font-family: "Exo 2", Arial, sans-serif;
  }
  .label {
    position: absolute;
    left: 240px;
    top: 130px;
    width: 720px;
    height: 700px;
    background: var(--label-black);
    overflow: hidden;
  }
  .claim-band {
    position: absolute;
    left: 0; top: 0;
    width: 100%;
    height: 52px;
    background: linear-gradient(180deg, var(--silver-mid) 0%, var(--silver-light) 45%, var(--silver-mid) 100%);
    border-bottom: 3px solid var(--silver-dark);
    display: flex;
    align-items: center;
    justify-content: center;
    z-index: 5;
  }
  .claim-band__text {
    font-weight: 700;
    font-size: 31px;
    letter-spacing: 2px;
    color: var(--band-text);
  }
  .neon-pattern {
    position: absolute;
    left: 0; top: 52px;
    width: 100%;
    height: 648px;
    background:
      radial-gradient(ellipse 45% 55% at 82% 40%, rgba(34,198,230,0.45), transparent 70%),
      radial-gradient(ellipse 35% 40% at 25% 62%, rgba(224,37,156,0.55), transparent 70%),
      var(--label-black);
  }
  .model-photo {
    position: absolute;
    left: 0; top: 52px;
    width: 380px;
    height: 648px;
    background:
      radial-gradient(ellipse 60% 45% at 45% 70%, var(--skin-warm), transparent 75%),
      radial-gradient(ellipse 50% 30% at 40% 18%, #a88570, transparent 75%),
      linear-gradient(180deg, #3a2a2a 0%, var(--skin-shadow) 60%, #1a0b12 100%);
    -webkit-mask-image: linear-gradient(90deg, #000 55%, transparent 100%);
            mask-image: linear-gradient(90deg, #000 55%, transparent 100%);
    z-index: 1;
  }
  .product-name {
    position: absolute;
    left: 0; right: 0;
    top: 330px;
    display: flex;
    align-items: center;
    justify-content: center;
    gap: 16px;
    padding-left: 70px;
    z-index: 4;
  }
  .product-name__mark {
    width: 22px;
    height: 22px;
    background: var(--name-silver);
  }
  .product-name__text {
    font-weight: 700;
    font-size: 82px;
    line-height: 1;
    color: var(--name-silver);
  }
  .product-facts {
    position: absolute;
    left: 70px;
    bottom: 70px;
    color: var(--white);
    font-style: italic;
    font-weight: 800;
    z-index: 4;
  }
  .product-facts__type { font-size: 27px; line-height: 1.2; }
  .product-facts__count { font-size: 42px; line-height: 1.1; letter-spacing: 1px; }
  .peak-ribbon {
    position: absolute;
    right: -120px;
    bottom: 60px;
    width: 520px;
    height: 96px;
    transform: rotate(-45deg);
    background: linear-gradient(180deg, var(--silver-mid) 0%, var(--silver-light) 50%, var(--silver-dark) 100%);
    display: flex;
    flex-direction: column;
    align-items: center;
    justify-content: center;
    color: var(--ribbon-text);
    font-style: italic;
    font-weight: 800;
    text-transform: uppercase;
    z-index: 6;
  }
  .peak-ribbon__top { font-size: 21px; letter-spacing: 1px; line-height: 1.1; }
  .peak-ribbon__bottom { font-size: 30px; letter-spacing: 1px; line-height: 1.1; }
</style>
</head>
<body>
  <main class="label">
    <div class="claim-band">
      <span class="claim-band__text">Enhances sexual desire</span>
    </div>

    <div class="neon-pattern" role="img" aria-label="Glowing cyan and magenta neon tile pattern on black"></div>
    <div class="model-photo" role="img" aria-label="Photograph of a woman looking back over her bare shoulder, lit in pink"></div>

    <div class="product-name">
      <span class="product-name__mark"></span>
      <h1 class="product-name__text">Velvet Crest</h1>
    </div>

    <div class="product-facts">
      <p class="product-facts__type">Dietary Supplement</p>
      <p class="product-facts__count">60 Capsules</p>
    </div>

    <div class="peak-ribbon">
      <span class="peak-ribbon__top">Reach your peak</span>
      <span class="peak-ribbon__bottom">Performance</span>
    </div>
  </main>
</body>
</html>
```